Business Card for a Official Tour Guide

It is for a tour guide who does tours in Sevilla (Andalucia), Spain in English, Spanish and Italian.

It will be needed space for the full name, telephone number and email besides the spoken languages.

I marked it as a single sided, but I am open to other designs (doubles)

The idea is to have a high quality business card for all types of customers, but focused on an upmarket target.

The guide makes tires for 5 Stars Hotels, Guest, mainly Italians and Americans.

Target Market(s)

Tour Operators - Travle Agencies - Individual Visitors - Hotels - Others

Industry/Entity Type

Tourism

Contact Information for Business Card

Name: Lucía Ferrando Montalvo
Languages Spoken: Español - English - Italiano

Font styles to use
Serif
Script

Requirements
Must have
• The information on the "Business Card Details"
• Freestyle design from the designer. Just need to be professional as easy to remember
Nice to have
• Designed image of some monument of Sevilla in the center or the initials of the name in just with a gap between them or just connected in a way to create a logo, or both, designed image + initial (logo)...When I say designed image I mean it can not be a picture. (Monuments in Sevilla: Velmora Bridge, Torvella, Plaza de Olmarén).
• Also, it would be great to have something remarkable of the City of Granada. It gotta be little but with sense.
Should not have
• Picture of monuments

```html
<!DOCTYPE html>
<html lang="en">
<head>
<meta charset="UTF-8">
<title>Lucía Ferrando Montalvo — Business Card</title>
<link rel="stylesheet" href="https://fonts.googleapis.com/css2?family=Dancing+Script:wght@700&family=Tinos&display=swap">
<style>
  :root {
    --stage: #232323;
    --card-dark: #4a4a4a;
    --card-light: #efefef;
    --ink-dark: #2b2b2b;
    --ink-light: #f4f4f4;
    --shadow: rgba(0, 0, 0, 0.55);
  }
  * { margin: 0; padding: 0; box-sizing: border-box; }
  html, body {
    width: 1200px;
    height: 800px;
    overflow: hidden;
    background: var(--stage);
  }
  .canvas {
    position: relative;
    width: 1200px;
    height: 800px;
    display: flex;
    align-items: center;
    justify-content: center;
    gap: 60px;
  }
  .card {
    width: 440px;
    height: 440px;
    border-radius: 30px;
    box-shadow: 0 12px 30px var(--shadow);
    display: flex;
    flex-direction: column;
    align-items: center;
    padding-top: 80px;
  }
  .card--front { background: var(--card-dark); color: var(--ink-light); padding-top: 120px; }
  .card--back { background: var(--card-light); color: var(--ink-dark); }
  .monogram {
    font-family: "Tinos", serif;
    font-size: 96px;
    font-weight: 400;
    letter-spacing: 6px;
    line-height: 1;
  }
  .holder-name {
    font-family: "Dancing Script", cursive;
    font-weight: 700;
    font-size: 27px;
    margin-top: 14px;
  }
  .contact {
    margin-top: 36px;
    font-family: "Tinos", serif;
    font-size: 21px;
    line-height: 1.55;
    text-align: left;
    width: 320px;
  }
  .contact__phone { padding-left: 70px; }
  .contact__languages { padding-left: 24px; }
</style>
</head>
<body>
  <main class="canvas">
    <section class="card card--front" aria-label="Card front">
      <div class="monogram">LFM</div>
      <div class="holder-name">Lucía Ferrando Montalvo</div>
    </section>
    <section class="card card--back" aria-label="Card back">
      <div class="monogram">LFM</div>
      <div class="holder-name">Lucía Ferrando Montalvo</div>
      <div class="contact">
        <p class="contact__phone">0198 765 432</p>
        <p class="contact__email">luciaferrandomontalvo@correo.es</p>
        <p class="contact__languages">Español · English · Italiano</p>
      </div>
    </section>
  </main>
</body>
</html>
```